Flyer/Poster design required for volunteer activities

We need a STRIKING A4 Poster/Flyer advertising our conservation volunteer program activities which are currently happening in the area. This poster is to advertise the program once people have arrived on the island or to locals. The program covers 5 months, May-September 2019 and is focused on conservation. I have attached the following:
- a flyer which was previously created (QMR Habitat Helpers 2019 sm)to advertise the program - would prefer it has a similar striking resemblance, but not essential
- A mock up document 'HHQMR On Island Poster_2019_v2' with text -Logos-Images

Target Market(s)

Everyone interested in Environmental Adventure/Hiking/Citizen Science

Industry/Entity Type

Tourism

Font styles to use
Sans Serif

Requirements
Must have
• -A travel conservation focus
• -Must use 'QMR-Background Image' as the background to the design
• -The info of where to get more information and the social media details must be prominent

```html
<!DOCTYPE html>
<html lang="en">
<head>
<meta charset="utf-8">
<title>QMR Habitat Helpers 2019 Poster</title>
<link href="https://fonts.googleapis.com/css2?family=Titan+One&family=Oswald:wght@500&family=Arimo:wght@400;700&display=swap" rel="stylesheet">
<style>
:root{
  --stage:#2b2b2b;
  --navy:#1f3f86;
  --green:#3aa63f;
  --band:#49a83f;
  --yellow:#f4ea1c;
  --white:#ffffff;
  --ink:#1a1a1a;
  --tile:#3a3a3a;
}
*{margin:0;padding:0;box-sizing:border-box}
html,body{width:720px;height:1200px;overflow:hidden;background:var(--stage)}
.poster{position:absolute;left:0;top:80px;width:792px;height:1144px;transform:scale(0.9091);transform-origin:0 0;overflow:hidden;font-family:"Arimo",Arial,sans-serif;color:var(--white)}
.backdrop{position:absolute;inset:0}
.abs{position:absolute}
.tagline{left:300px;top:28px;width:420px;text-align:center;font-family:"Oswald",sans-serif;color:var(--green);font-size:31px;line-height:34px;letter-spacing:.5px}
.brand{left:28px;top:21px;width:206px;height:206px;border-radius:50%;border:6px solid var(--navy);background:rgba(255,255,255,.85);display:flex;align-items:center;justify-content:center;text-align:center;font-weight:700;color:var(--navy);font-size:24px;line-height:28px;padding:20px}
.title{left:100px;top:172px;width:636px;transform:rotate(-7deg);transform-origin:100% 50%;text-align:right;font-family:"Titan One",sans-serif;color:var(--navy);letter-spacing:1px}
.title .l1{font-size:54px;line-height:56px}
.title .l2{font-size:50px;line-height:52px}
.join{left:350px;top:288px;width:401px;transform:rotate(-7deg);transform-origin:100% 50%;text-align:right;font-weight:700;font-size:22px;line-height:25px}
.join .y{color:var(--yellow)}
.join .dates{font-size:19px}
.photo{width:157px;height:140px;border:7px solid var(--yellow)}
.month{width:190px;text-align:center;font-weight:700;font-size:13.5px;line-height:15px}
.month .m{font-size:16px;line-height:18px}
.col{width:182px;text-align:center;font-weight:700;font-size:12.5px;line-height:14px}
.col .h{font-size:13.5px}
.para{left:190px;top:791px;width:292px;text-align:center;font-weight:700;font-size:12.5px;line-height:14px}
.follow{left:588px;top:862px;transform:rotate(-32deg);font-family:"Titan One",sans-serif;font-size:30px;color:var(--white)}
.social-tile{width:68px;height:58px;background:var(--tile);border-radius:4px}
.handle{right:38px;text-align:right;font-weight:700;font-size:22px;color:var(--ink);white-space:nowrap}
.info{left:40px;top:1046px;width:350px;text-align:center;color:var(--ink);font-weight:700;font-size:17px;line-height:24px}
</style>
</head>
<body>
<div class="poster">
  <svg class="backdrop" width="792" height="1144" viewBox="0 0 792 1144">
    <defs>
      <linearGradient id="scene" x1="0" y1="0" x2="0" y2="1">
        <stop offset="0" stop-color="#cfe2ef"/>
        <stop offset=".28" stop-color="#8fb5c8"/>
        <stop offset=".45" stop-color="#3d8aa6"/>
        <stop offset=".7" stop-color="#2a6684"/>
        <stop offset="1" stop-color="#4d7b6a"/>
      </linearGradient>
    </defs>
    <rect width="792" height="1144" fill="url(#scene)" role="img" aria-label="Photo of the island mountains, lagoon and reef from above"/>
    <path d="M0 516 Q400 504 792 516 L792 572 L0 572 Z" fill="var(--band)"/>
    <path d="M0 950 C200 1060 520 1040 792 812 L792 1144 L0 1144 Z" fill="var(--band)"/>
    <path d="M0 975 C210 1082 530 1062 792 838 L792 1144 L0 1144 Z" fill="var(--yellow)"/>
  </svg>

  <div class="abs tagline">BE INVOLVED IN PROTECTING<br>PARADISE</div>
  <div class="abs brand">QMR Habitat Helpers</div>

  <div class="abs title"><div class="l1">QUEEN MIRA REEF</div><div class="l2">HABITAT HELPERS</div></div>
  <div class="abs join"><span class="y">JOIN THE</span> QMR HABITAT<br>HELPERS <span class="y">PROGRAM 2019</span><br><span class="dates">May – September 2019</span></div>

  <div class="abs photo" style="left:12px;top:381px;background:#7b8a6a" role="img" aria-label="Photo of a seabird resting in grass"></div>
  <div class="abs photo" style="left:204px;top:381px;background:#3f9fc4" role="img" aria-label="Photo of a snorkeller recording data underwater"></div>
  <div class="abs photo" style="left:408px;top:381px;background:#4a5a3a" role="img" aria-label="Photo of a walker on a forest track"></div>
  <div class="abs photo" style="left:618px;top:385px;background:#b09078" role="img" aria-label="Photo of a large stick insect on a hand"></div>
  <div class="abs photo" style="left:13px;top:773px;background:#8fb0c8" role="img" aria-label="Photo of a hiker on a coastal lookout"></div>

  <div class="abs month" style="left:-8px;top:523px"><div class="m">MAY 2019</div>Feature Week:<br>19th – 26th May</div>
  <div class="abs month" style="left:180px;top:528px"><div class="m">JUNE 2019</div>Feature Week:<br>3rd– 9th June</div>
  <div class="abs month" style="left:405px;top:524px"><div class="m">JULY 2019</div>Feature Week:<br>21st – 28th July</div>
  <div class="abs month" style="left:603px;top:524px"><div class="m">AUGUST 2019</div>Feature Week:<br>11th-19th August</div>

  <div class="abs col" style="left:16px;top:578px"><span class="h">BIRDS OF QUEEN MIRA REEF</span><br>-Ocean bird watching boat trips<br>-Guided tours of Woodhen and Currawong quarters<br>-Weekly lectures at the Queen Mira Reef Museum<br>-Weekly screenings of documentaries on Bird and Island Conservation projects<br>-Self guided land bird survey tours</div>
  <div class="abs col" style="left:211px;top:578px"><span class="h">QUEEN MIRA REEF<br>MARINE PARK</span><br>-Marine pest monitoring with marine park staff<br>-Marine plastic &amp; debris clean up activities<br>-Screenings of marine conservation documentaries at the museum<br>-Weekly lectures on Marine Life at the Queen Mira Reef Museum<br>-Marine Activities with local operators</div>
  <div class="abs col" style="left:405px;top:578px"><span class="h">INVASIVE SPECIES</span><br>-Guided walks to learn about the weed eradication program<br>-Weekly lectures on plants of Queen Mira Reef<br>-Weekly screenings of documentaries on plant and island conservation projects<br>-Guided walks to Mount Tarrow<br>-Local tour guides include commentaries on island plants</div>
  <div class="abs col" style="left:592px;top:576px"><span class="h">AMAZING INVERTEBRATES</span><br>-Guided night walks to learn about the island's invertebrates<br>-Weekly viewing and presentation of the Queen Mira Reef Phasmid<br>-Weekly lectures on invertebrates of Queen Mira Reef at the museum<br>-Weekly screenings of documentaries on island conservation projects</div>

  <div class="abs para"><span style="font-size:14px">PROTECTING PARADISE</span><br>-Observational snorkel surveys with Marine Ecologists, to assess populations of McCulloch's Anemonefish and other unique fish species<br>-Guided snorkel and glass bottom boat tour to assess coral health within the Queen Mira Reef Marine Park<br>-Guided walks to learn about the island's conservation history</div>

  <div class="abs month" style="left:0;top:929px"><div class="m" style="font-size:14px;line-height:15px">SEPTEMBER 2019</div>Feature Week: 1st-8th<br>September</div>

  <div class="abs follow">FOLLOW US!</div>
  <div class="abs social-tile" style="left:688px;top:941px"></div>
  <div class="abs handle" style="top:1012px">pixlens@hhqmr</div>
  <div class="abs social-tile" style="left:478px;top:1024px"></div>
  <div class="abs handle" style="top:1081px">www.friendloop.com/hhqmr</div>

  <div class="abs info">See the <b style="font-size:19px">QMR Visitor Centre</b> for more information about the QMR Habitat Helpers program for 2019</div>
</div>
</body>
</html>
```